Website Redesign - We Need Your Magic!

Hello we are looking for you to help us re-design a high end and professional website for a high-end private school.

Here is the current site: http://www.brevanholt.example/

NOTE THIS IS DESIGN ONLY, NO CODING :)

The image they want to portray is that of high quality sports and education, in a creative "un-stiff" way.

Menu Bar: Horizontal

Look and Feel:

Site Colors: Dark green and a Gold yellow (logos are attached)

This site will represent a school so the look must be clean, bold, and classy. The site must have a very clean user interface, with things easily recognizable. Think simple.

The site should be visually appealing! If you come to me with templates, or a ton of text you will be out.

This site should be outside the box, we do not want boring, we do not want status quo. This site should instill excitement, innovation, and athletics.

So the main points again are:

1. High-end and classy look, with creative feel
2. Simple and clear navigation style
3. To cover the Junior and High School - Brevanholt College Schools

Think outside the box. We look forward to seeing what you come up with!!

Thank you for helping us create an amazing site for the school!

Industry/Entity Type

School

```html
<!DOCTYPE html>
<html lang="en">
<head>
<meta charset="utf-8">
<title>Brevanholt College</title>
<link rel="stylesheet" href="https://fonts.googleapis.com/css2?family=Carlito:wght@400;700&family=Russo+One&display=swap">
<style>
  :root {
    --gold: #c09a2c;
    --green-dark: #14280f;
    --ink: #1e1e1e;
    --white: #ffffff;
    --rule: #2b2b2b;
    --widget-border: #c9ccd3;
    --body-font: "Carlito", "Calibri", sans-serif;
    --display-font: "Russo One", sans-serif;
  }
  * { margin: 0; padding: 0; box-sizing: border-box; }
  html, body { width: 1200px; height: 1000px; overflow: hidden; background: var(--white); }
  body { position: relative; font-family: var(--body-font); color: var(--ink); }
  .abs { position: absolute; }

  .site-header { left: 262px; top: 2px; width: 640px; height: 99px; background: var(--gold); }
  .brand { left: 18px; top: 34px; display: flex; align-items: center; gap: 8px; }
  .brand-mark { width: 26px; height: 26px; background: var(--green-dark); }
  .brand-name { font-size: 19px; font-weight: 400; color: var(--green-dark); letter-spacing: 0.5px; line-height: 1; }
  .brand-tagline { left: 60px; top: 58px; font-size: 7.5px; font-weight: 700; color: var(--green-dark); white-space: nowrap; }
  .main-nav { top: 47px; font-size: 10px; color: var(--green-dark); }
  .main-nav span { position: absolute; white-space: nowrap; }

  .hero { left: 262px; top: 101px; width: 640px; height: 328px;
    background: linear-gradient(180deg, #2f3a2c 0%, #46523f 45%, #4d7a2d 80%, #5a8a30 100%); }
  .hero-rule { left: 86px; width: 478px; height: 2px; background: var(--white); }
  .hero-title { left: 0; width: 640px; top: 136px; text-align: center; font-family: var(--display-font);
    color: var(--white); font-size: 27px; letter-spacing: 3px; line-height: 39px; }

  .intro-bar { width: 2px; height: 66px; background: var(--gold); top: 466px; }
  .intro-heading { font-size: 31px; color: var(--green-dark); line-height: 1; }
  .intro-text { font-size: 9.5px; line-height: 11.5px; color: var(--ink); width: 260px; }

  .news-heading { left: 262px; width: 640px; top: 561px; text-align: center; font-size: 15px; color: var(--green-dark); }
  .news-text { left: 262px; width: 640px; top: 582px; text-align: center; font-size: 8px; line-height: 10px; }
  .news-photo { top: 632px; width: 159px; height: 95px; }

  .headmaster { left: 262px; top: 747px; width: 640px; height: 110px; background: var(--gold); text-align: center; }
  .headmaster h2 { font-weight: 400; font-size: 22px; color: var(--green-dark); margin-top: 24px; }
  .headmaster p { font-size: 8px; line-height: 10.5px; color: var(--green-dark); width: 360px; margin: 4px auto 0; }

  .contact { left: 420px; width: 222px; top: 882px; text-align: center; }
  .contact h3 { font-weight: 400; font-size: 13.5px; color: var(--green-dark); letter-spacing: 0.3px; }
  .contact p { font-size: 8px; line-height: 9.5px; margin-top: 3px; }
  .social-links { left: 465px; top: 938px; display: flex; gap: 7px; }
  .social-links span { width: 21px; height: 21px; background: var(--green-dark); display: block; }
  .social-links .round { border-radius: 50%; }

  .social-widget { left: 651px; top: 864px; width: 89px; height: 104px; border: 1px solid var(--widget-border); background: #fff; }
  .widget-top { height: 11px; background: #eef0f4; border-bottom: 1px solid var(--widget-border); font-size: 5px; font-weight: 700; padding: 3px 3px 0; color: #333; }
  .widget-page { display: flex; align-items: center; gap: 3px; padding: 4px 5px 0; font-size: 4px; font-weight: 700; color: #333; }
  .widget-page i { width: 10px; height: 10px; background: var(--green-dark); display: block; }
  .widget-likes { font-size: 4px; padding: 6px 4px 2px; color: #333; }
  .widget-faces { display: grid; grid-template-columns: repeat(4, 17px); gap: 2px 2px; padding: 0 4px; }
  .widget-faces div { font-size: 3.5px; text-align: center; color: #555; }
  .widget-faces b { display: block; width: 17px; height: 16px; background: #8e8a80; }
  .widget-foot { font-size: 3.5px; padding: 3px 4px; color: #555; }

  .footer-rule { left: 332px; top: 969px; width: 528px; height: 2px; background: var(--rule); }
  .footer-note { left: 332px; width: 528px; top: 977px; text-align: center; font-size: 5px; color: var(--ink); }
</style>
</head>
<body>

<header class="abs site-header">
  <div class="abs brand">
    <span class="brand-mark"></span>
    <span class="brand-name">BREVANHOLT COLLEGE</span>
  </div>
  <div class="abs brand-tagline">Stepping Ahead in &nbsp;•&nbsp; Education &nbsp;•&nbsp; Culture &nbsp;•&nbsp; Sport &nbsp;•&nbsp; Life</div>
  <nav class="abs main-nav">
    <span style="left:272px">Home</span>
    <span style="left:310px">About Us</span>
    <span style="left:358px">Academics</span>
    <span style="left:414px;top:2px">Sports</span>
    <span style="left:455px">Working at the College</span>
    <span style="left:561px">Contact Us</span>
  </nav>
</header>

<section class="abs hero" role="img" aria-label="Photo of young children running with rugby balls across a green sports field">
  <div class="abs hero-rule" style="top:134px"></div>
  <h1 class="abs hero-title">PROVIDING HIGH QUALITY SPORTS<br>AND EDUCATION.</h1>
  <div class="abs hero-rule" style="top:211px"></div>
</section>

<div class="abs intro-bar" style="left:287px"></div>
<h2 class="abs intro-heading" style="left:302px;top:463px;font-weight:400">WELCOME!</h2>
<p class="abs intro-text" style="left:303px;top:497px">Welcome to Brevanholt Group of Schools where our School Motto is ‘Tabatana’ meaning Togetherness. We aim to work together in every aspect of School life, from academics to sport.</p>

<div class="abs intro-bar" style="left:594px;top:463px"></div>
<h2 class="abs intro-heading" style="left:609px;top:459px;font-weight:400">OUR MISSION</h2>
<p class="abs intro-text" style="left:611px;top:494px;width:270px">We are an English-speaking Christian School aspiring to the highest international standards academically, in technical and commercial education, in sporting endeavour and culturally.</p>

<h3 class="abs news-heading" style="font-weight:400">CURRENT NEWS:</h3>
<p class="abs news-text">On the sports fields last year twenty-eight of our pupils were selected for various national sides.<br>We introduced two new sports this year; Triathlon and Mountain biking.</p>

<div class="abs news-photo" style="left:307px;background:linear-gradient(160deg,#d9ddd6,#9fae8a 60%,#6f8f3e)" role="img" aria-label="Photo of a goalkeeper diving for a football in front of a net"></div>
<div class="abs news-photo" style="left:502px;background:linear-gradient(180deg,#8fa47a,#7f8480 55%,#6e706f)" role="img" aria-label="Photo of children cycling along a park road"></div>
<div class="abs news-photo" style="left:689px;background:linear-gradient(160deg,#b8866a,#7a3b3b 55%,#c49a6a)" role="img" aria-label="Photo of a girls' basketball team huddled together"></div>

<section class="abs headmaster">
  <h2>Headmaster's Welcome Note</h2>
  <p>Welcome to Brevanholt College. &nbsp;Here at the College we aim to encourage each pupil to be a self-confident, well-rounded individual. &nbsp;We aim to propel them to the highest level of achievement in both academics and extra-curricular activities to provide them with the life skills they will need when they leave the College and to prepare them to be of value to society.</p>
</section>

<section class="abs contact">
  <h3>GET IN TOUCH</h3>
  <p>Lorem ipsum dolor sit amet, consectetur adipiscing elit.<br>Maurissemper eu turpis sed, mollis vehicula neque.<br>Ut in urna ante. Etiam sit amet arcu ante.</p>
</section>
<div class="abs social-links" aria-label="Social links">
  <span></span><span class="round"></span><span></span><span></span><span></span>
</div>

<aside class="abs social-widget">
  <div class="widget-top">Find us on Friendwall</div>
  <div class="widget-page"><i></i><span>BREVANHOLT COLLEGE</span></div>
  <div class="widget-likes">190 people like Harlow Sales.</div>
  <div class="widget-faces">
    <div><b></b>Paul</div><div><b></b>Milo</div><div><b></b>Mark</div><div><b></b>Adam</div>
    <div><b></b>Brad</div><div><b></b>Jonah</div><div><b></b>Sara</div><div><b></b>Jane</div>
  </div>
  <div class="widget-foot">Social plugin</div>
</aside>

<div class="abs footer-rule"></div>
<div class="abs footer-note">BREVANHOLT COLLEGE© 2014 | PRIVACY POLICY</div>

</body>
</html>
```